Envelope Design Project for Real Estate

I am looking for an envelope design for a real estate brokerage. I prefer muted colors and the primary colors should be white, maroon (884445) and gray (aaaaaa).
The design is for a #10 universal envelope (psd and jpg files attached for guidelines). There should be full color on the front and back of the envelope.
You can add a return address on the back side along the top flap. Please use a sample address and phone number in the design - the actual information will be provided to the winning designer.

```html
<!DOCTYPE html>
<html lang="en">
<head>
<meta charset="utf-8">
<title>Birch Hollow Realty – #10 Envelope</title>
<link rel="stylesheet" href="https://fonts.googleapis.com/css2?family=Open+Sans:wght@400;600&display=swap">
<style>
  :root {
    --maroon: #884445;
    --gray: #aaaaaa;
    --white: #ffffff;
    --backdrop: #2b2b2b;
  }
  html, body {
    margin: 0;
    padding: 0;
    width: 1200px;
    height: 750px;
    overflow: hidden;
    background: var(--backdrop);
  }
  .canvas {
    position: relative;
    width: 1200px;
    height: 750px;
  }
  .envelope {
    position: absolute;
    left: 100px;
    top: 157px;
    width: 1000px;
    height: 436px;
    background: var(--white);
    overflow: hidden;
    box-shadow: 0 6px 18px rgba(0,0,0,0.35);
  }
  .envelope-art {
    position: absolute;
    inset: 0;
    width: 100%;
    height: 100%;
  }
  .art-maroon { fill: var(--maroon); }
  .art-stripe { fill: var(--gray); }
  .brand {
    position: absolute;
    left: 40px;
    top: 52px;
    display: flex;
    align-items: center;
    gap: 12px;
  }
  .brand-dot {
    width: 44px;
    height: 44px;
    border-radius: 50%;
    background: var(--white);
  }
  .brand-name {
    font-family: "Open Sans", sans-serif;
    font-weight: 600;
    font-size: 22px;
    color: var(--white);
    letter-spacing: 0.5px;
  }
  .return-address {
    position: absolute;
    left: 40px;
    bottom: 26px;
    margin: 0;
    font-family: "Open Sans", sans-serif;
    font-style: normal;
    font-size: 14px;
    line-height: 1.45;
    color: var(--white);
  }
  .return-address .label { margin-right: 14px; }
</style>
</head>
<body>
<main class="canvas">
  <section class="envelope" aria-label="Envelope front">
    <svg class="envelope-art" viewBox="0 0 1000 436" preserveAspectRatio="none" aria-hidden="true">
      <path class="art-maroon" d="M0,0 L600,0 C720,80 800,250 850,436 L0,436 Z"/>
      <path class="art-stripe" d="M600,0 L628,0 C748,80 826,250 876,436 L850,436 C800,250 720,80 600,0 Z"/>
    </svg>
    <div class="brand">
      <span class="brand-dot"></span>
      <span class="brand-name">Birch Hollow Realty</span>
    </div>
    <address class="return-address">
      Lena Morrow, Lindenweg 12/B204, 1140 Wien<br>
      <span class="label">Tel.:</span>+43 699 480 215 36, hello@lenamorrow.com, www.birchhollowrealty.com
    </address>
  </section>
</main>
</body>
</html>
```